Landing page graphical layout.

New landing page to capture leads from homeowners who are interested in learning the value of their home and/or selling their home.
The page should have a picture of a home in a residential area, possibly with a family standing outside.
This is the client's current site: http://homeworthpulse.com/
As you can see, it is very limited in terms of text and design, however once the user fills in the field it takes them to another page. The page's graphics should be enhanced with more calls to action as well as an additional field for the email address.
The client is a lead generator for real estate agents, so do not put the company name on the site as it will be used as a template for the client's various sites.
The forms need to be duplicated and inserted into the new design.
Some example sites:
http://www.brindlo.com/how-much-is-my-home-worth/
http://www.kptroost.com/home-valuation/?source=PROMO_SELLER&gclid=XQwerT_b-zzKLMnopqrS4B1
https://www.plovara.com/what-is-my-home-worth?estPropertyId=4190827&src=landing-page
Thanks!
Industry/Entity Type
Real Estate
Number of Pages Required
1 page
Look and feel

```html
<!DOCTYPE html>
<html lang="en">
<head>
<meta charset="utf-8">
<title>Get Your Home Value Estimate</title>
<link rel="stylesheet" href="https://fonts.googleapis.com/css2?family=Oswald:wght@300;400;500&family=Open+Sans:wght@400;600;700&display=swap">
<style>
:root{
  --ink:#2b2b2b;
  --band:#2a2a2c;
  --sky:#2f9be2;
  --sky-deep:#1f82c9;
  --step-box:#1e4f95;
  --navy:#12388a;
  --navy-box:#25489c;
  --mist:#e6e6e6;
  --white:#ffffff;
  --field-line:#c9c9c9;
  --muted:#6b6b6b;
  --button:#1e4f95;
}
*{box-sizing:border-box;margin:0;padding:0}
html,body{width:1200px;height:2608px;overflow:hidden}
body{font-family:"Open Sans",Arial,sans-serif;color:var(--ink);background:var(--white);position:relative}

.hero{position:absolute;left:0;top:0;width:1200px;height:850px}
.hero-photo{position:absolute;left:0;top:0;width:1200px;height:740px;
  background:linear-gradient(180deg,#c9d3cf 0%,#a9b59a 38%,#6f8b4c 70%,#8a5a3e 100%)}
.hero-band{position:absolute;left:0;top:740px;width:1200px;height:110px;background:var(--band);
  display:flex;align-items:center;justify-content:center}
.hero-title{font-family:"Oswald",Arial,sans-serif;font-weight:400;font-size:46px;letter-spacing:2px;color:var(--white);text-transform:uppercase;margin-top:10px}
.hero-badge{position:absolute;left:540px;top:650px;width:120px;height:120px;border-radius:50%;background:var(--band);
  display:flex;align-items:center;justify-content:center}

.step{position:absolute;left:0;width:1200px}
.step-head{position:absolute;left:120px;top:10px;display:flex;align-items:center}
.step-tag{width:184px;height:66px;background:var(--step-box);color:var(--white);
  font-family:"Oswald",Arial,sans-serif;font-size:38px;font-weight:400;display:flex;align-items:center;justify-content:center;letter-spacing:1px}
.step-title{font-family:"Oswald",Arial,sans-serif;font-weight:300;font-size:36px;color:var(--white);margin-left:20px;text-transform:uppercase;letter-spacing:1px}
.step-note{position:absolute;left:324px;top:66px;font-size:17px;color:var(--muted)}
.toggle{position:absolute;right:120px;bottom:-44px;width:88px;height:88px;border-radius:50%;background:var(--mist);
  display:flex;align-items:flex-end;justify-content:center;padding-bottom:18px;z-index:2}

.step-address{top:850px;height:350px;background:linear-gradient(135deg,var(--sky) 0%,var(--sky-deep) 100%)}
.address-form{position:absolute;left:220px;top:170px;width:756px;height:60px;background:var(--white);display:flex;align-items:center}
.address-form input{border:0;outline:0;flex:1;height:100%;padding:0 20px;font:16px "Open Sans",Arial,sans-serif;color:var(--muted);background:transparent}
.address-form .search{width:60px;display:flex;align-items:center;justify-content:center}

.step-info{top:1200px;height:440px;background:var(--mist)}
.step-info .step-title{color:#3a3a3a}
.toggle-light{background:#d0d0d0}
.toggle-on-navy{background:var(--mist)}
.info-form{position:absolute;left:120px;top:128px;width:232px}
.info-form label{display:block;font-size:11px;color:#4a4a4a;margin-bottom:3px}
.info-form .cell{height:28px;background:var(--white);border:1px solid var(--field-line);font-size:11px;color:var(--muted);padding:0 8px;display:flex;align-items:center;margin-bottom:8px}
.info-row{display:flex;gap:12px}
.info-row>div{flex:1}
.confirm{width:100%;height:30px;background:var(--button);color:var(--white);border:0;font:700 12px "Open Sans",Arial,sans-serif;text-transform:uppercase;margin-top:4px}
.home-photo{position:absolute;left:368px;top:132px;width:712px;height:260px;
  background:linear-gradient(90deg,#8a4a32 0%,#6d7a4a 40%,#b9b2a4 70%,#7f3c2c 100%)}

.step-value{top:1640px;height:348px;background:var(--navy)}
.step-value .step-tag{background:var(--navy-box)}
.value-address{position:absolute;left:150px;top:112px;display:flex;align-items:center;gap:18px;color:var(--white);font-size:17px}
.value-note{position:absolute;left:0;width:1200px;top:212px;text-align:center;color:var(--white);font-weight:700;font-size:18px}
.value-box{position:absolute;left:408px;top:248px;width:384px;height:62px;border:2px solid var(--white);
  display:flex;align-items:center;justify-content:center;color:var(--white);font-size:20px;font-weight:600}

.consult{position:absolute;left:0;top:1988px;width:1200px;height:524px;background:var(--white)}
.consult-title{position:absolute;left:0;top:30px;width:1200px;text-align:center;font-family:"Oswald",Arial,sans-serif;font-weight:400;font-size:40px;color:var(--step-box);text-transform:uppercase}
.consult-lead{position:absolute;left:300px;top:100px;width:600px;text-align:center;font-size:17px;line-height:25px;color:#444}
.consult-form{position:absolute;left:264px;top:184px;width:676px}
.field{height:40px;border:1px solid var(--field-line);background:var(--white);font-size:13px;color:#999;padding:0 12px;display:flex;align-items:center}
.field-row{display:flex;gap:12px;margin-bottom:16px}
.field-row .field{flex:1}
.field-label{font-size:13px;color:#444;margin:-4px 0 6px}
.field-wide{margin-bottom:16px}
.field-area{height:78px;align-items:flex-start;padding-top:10px}
.send{position:absolute;left:236px;top:268px;width:204px;height:44px;background:var(--button);color:var(--white);border:0;
  font:600 18px "Open Sans",Arial,sans-serif;text-transform:uppercase;letter-spacing:1px}
.consult-form .send{top:424px}

.footer{position:absolute;left:0;top:2512px;width:1200px;height:96px;background:var(--band);display:flex;align-items:center;justify-content:center;color:#bdbdbd;font-size:15px}
</style>
</head>
<body>

<header class="hero">
  <div class="hero-photo" role="img" aria-label="Smiling family of four standing outside their house in a leafy residential street"></div>
  <div class="hero-band"><h1 class="hero-title">Get your home value estimate</h1></div>
  <div class="hero-badge">
    <svg width="62" height="54" viewBox="0 0 62 54" aria-hidden="true">
      <path d="M31 2 L2 28 h9 v24 h15 v-15 h10 v15 h15 v-24 h9 z" fill="#fff"/>
    </svg>
  </div>
</header>

<section class="step step-address">
  <div class="step-head"><span class="step-tag">STEP 1</span><h2 class="step-title">Your address</h2></div>
  <form class="address-form">
    <input type="text" placeholder="Your Address" aria-label="Your address">
    <span class="search">
      <svg width="28" height="28" viewBox="0 0 28 28" aria-hidden="true"><circle cx="11" cy="11" r="8" fill="none" stroke="#2b2b2b" stroke-width="3.5"/><path d="M17 17 L25 25" stroke="#2b2b2b" stroke-width="4" stroke-linecap="round"/></svg>
    </span>
  </form>
  <span class="toggle">
    <svg width="28" height="16" viewBox="0 0 28 16" aria-hidden="true"><path d="M3 3 L14 13 L25 3" fill="none" stroke="#2f9be2" stroke-width="4"/></svg>
  </span>
</section>

<section class="step step-info">
  <div class="step-head"><span class="step-tag">STEP 2</span><h2 class="step-title">Home information</h2></div>
  <p class="step-note">Find your home value right now by simply confirming information about your home.</p>
  <form class="info-form">
    <label>Property Type</label>
    <div class="cell">Single family home</div>
    <div class="info-row">
      <div><label>Bedrooms</label><div class="cell">3</div></div>
      <div><label>Bathrooms</label><div class="cell">2</div></div>
    </div>
    <div class="info-row">
      <div><label>Square footage</label><div class="cell">1850</div></div>
      <div><label>Lot size</label><div class="cell">0.25</div></div>
    </div>
    <div class="info-row">
      <div><label>Year built</label><div class="cell">1985</div></div>
      <div><label>Condition</label><div class="cell">Good</div></div>
    </div>
    <button class="confirm" type="button">Confirm your details</button>
  </form>
  <div class="home-photo" role="img" aria-label="Brick houses along a quiet tree-lined lane"></div>
  <span class="toggle toggle-light">
    <svg width="28" height="16" viewBox="0 0 28 16" aria-hidden="true"><path d="M3 3 L14 13 L25 3" fill="none" stroke="#8a8a8a" stroke-width="4"/></svg>
  </span>
</section>

<section class="step step-value">
  <div class="step-head"><span class="step-tag">STEP 3</span><h2 class="step-title">Home value</h2></div>
  <div class="value-address">
    <svg width="40" height="40" viewBox="0 0 40 40" aria-hidden="true"><circle cx="20" cy="20" r="18" fill="none" stroke="#fff" stroke-width="2.5"/><path d="M20 10 a6 6 0 0 1 6 6 c0 5 -6 13 -6 13 s-6 -8 -6 -13 a6 6 0 0 1 6 -6z" fill="#fff"/><circle cx="20" cy="16" r="2.2" fill="#12388a"/></svg>
    <span>5904 Harbor Lane E, Weston Park, NJ 07093, USA</span>
  </div>
  <p class="value-note">Check it out! Your home value is below</p>
  <div class="value-box">Price Estimate: &nbsp;$123:00 to $345:00 *</div>
</section>

<section class="consult">
  <h2 class="consult-title">Get a no-obligation consultation</h2>
  <p class="consult-lead">A Local Agent can send you a professional comparative market analysis (CMA) for this home. It's free, with no obligation</p>
  <form class="consult-form">
    <div class="field-row"><div class="field">First Name</div><div class="field">Last Name</div></div>
    <div class="field-row"><div class="field">Email</div><div class="field">Phone</div></div>
    <p class="field-label">Request a Professional CMA for</p>
    <div class="field field-wide"></div>
    <div class="field field-area">Comments/Notes</div>
    <button class="send" type="button">Send request</button>
  </form>
</section>

<footer class="footer">© 2015, All rights reserved.</footer>

</body>
</html>
```